Tranquil Harbour Hypnotherapy 2017 DL Card Flyer

We would like a double sided DL Card Flyer design.

We are a professional Hypnotherapy Clinic looking for a fresh clean design.

Front of card is summary info and back of flyer is detailed text.

I have attached documents with text for the front (dl size hypno 1) and back (dl size hypno 2) of the card and an indicative style of layout.

There are logo files uploaded as well as one image file.

The colors we like are blue, white and yellow/gold.
Updates

please note: when using the 'new mindset new results' image, please only use the top half of the image. The girl is not to be in the image, just the words and light bulb with the chalk underline. thanks.. Added Sunday, March 19, 2017

Industry/Entity Type

Health And Wellness

Requirements
Must have
• Note. I have misspelled the www.TranquilHarbourHypnotherapy.com.au (missing an 'o' in the attachments to the brief). My error. Please amend in your design submissions.

```html
<!DOCTYPE html>
<html lang="en">
<head>
<meta charset="utf-8">
<title>Tranquil Harbour Hypnotherapy – Programs</title>
<link href="https://fonts.googleapis.com/css2?family=Arimo:ital,wght@0,400;0,700;1,400;1,700&display=swap" rel="stylesheet">
<style>
  :root {
    --navy: #253f8f;
    --navy-text: #22409a;
    --gold: #f1c94b;
    --white: #ffffff;
    --ink: #2a2a2a;
    --gold-deep: #dcc257;
    --cream: #f7f1da;
  }
  * { margin: 0; padding: 0; box-sizing: border-box; }
  html, body { width: 1200px; height: 2400px; overflow: hidden; }
  body {
    font-family: "Arimo", Arial, sans-serif;
    background: linear-gradient(180deg, var(--gold-deep) 0%, #e4cf72 45%, #efe3ad 75%, var(--cream) 100%);
    position: relative;
  }
  .backdrop { position: absolute; inset: 0; }
  .program {
    position: absolute;
    left: 80px;
    width: 1040px;
    padding: 40px 30px 0 64px;
    box-shadow: 0 6px 14px rgba(60, 50, 10, 0.25);
    white-space: nowrap;
  }
  .program--light {
    background: var(--white);
    color: var(--ink);
    border-radius: 30px 60px 60px 0;
  }
  .program--dark {
    background: var(--navy);
    color: var(--white);
    border-radius: 60px 0 0 60px;
  }
  .program__title {
    font-size: 31px;
    font-weight: 700;
    line-height: 43px;
    margin-bottom: 10px;
  }
  .program--light .program__title { color: var(--navy-text); }
  .program--dark .program__title { color: var(--gold); }
  .program__text {
    font-size: 33px;
    line-height: 43px;
  }
  .program__sessions {
    font-size: 34px;
    font-weight: 700;
    line-height: 43px;
    margin-top: 17px;
  }
  .program--light .program__sessions { color: var(--navy-text); }
  .program--dark .program__sessions { color: var(--white); }

  .program--weight   { top: 99px;   height: 357px; z-index: 5; }
  .program--sugar    { top: 456px;  height: 403px; z-index: 4; }
  .program--smoking  { top: 859px;  height: 365px; z-index: 3; }
  .program--fatigue  { top: 1224px; height: 608px; z-index: 2; }
  .program--stress   { top: 1832px; height: 365px; z-index: 1; }

  .footer-note {
    position: absolute;
    top: 2247px;
    left: 0; right: 0;
    text-align: center;
    font-size: 27px;
    line-height: 43px;
    color: var(--ink);
  }
</style>
</head>
<body>
  <div class="backdrop" role="img" aria-label="Gold background with fine diagonal stripes fading to cream"></div>

  <section class="program program--light program--weight">
    <h2 class="program__title">WEIGHT LOSS PROGRAM (Mindful Portion Method)</h2>
    <p class="program__text">Achieve long term weight loss without dieting. Whether<br>it’s losing 3kg or 30kg, we’ll help you become the shape<br>and size you want to be. Our Internationally Accredited<br>Program is proven to be 95% effective in clinical trials.</p>
    <p class="program__sessions">Number of Sessions: 6+</p>
  </section>

  <section class="program program--dark program--sugar">
    <h2 class="program__title">SUGAR ADDICTION PROGRAM</h2>
    <p class="program__text">Excess sugar intake can lead to obesity, Type 2 Diabetes<br>and tooth decay. The habit of reaching for soft drinks,<br>chocolate, sweets, cakes and biscuits can be hard<br>to break. By rewiring your subconscious habits, our<br>Program puts you back in control.</p>
    <p class="program__sessions">Number of Sessions: 3+</p>
  </section>

  <section class="program program--light program--smoking">
    <h2 class="program__title">QUIT SMOKING PROGRAM</h2>
    <p class="program__text">The facts speak for themselves.&nbsp; You are 10 times more<br>likely to quit smoking for good using hypnotherapy.<br>Expect to be a non smoker after completing the first<br>session of our Program. (12 Month Guarantee)</p>
    <p class="program__sessions">Number of Sessions: 2</p>
  </section>

  <section class="program program--dark program--fatigue">
    <h2 class="program__title">CHRONIC FATIGUE &amp; CHRONIC PAIN RELIEF<br>PROGRAM</h2>
    <p class="program__text">Chronic Fatigue, Fibromyalgia and Chronic<br>Musculoskeletal Pain are diseases of modern living. The<br><em><strong>symptoms</strong></em> of fatigue and pain are very real, however<br>the <em><strong>cause</strong></em> is usually emotional, and is generally hidden<br>beyond our conscious awareness.<br>Our Program comprises Education and Hypnosis to help<br>you regain your health, your self esteem, your friends<br>and your life, all in a manageable timeframe.</p>
    <p class="program__sessions">Number of Sessions: 6+</p>
  </section>

  <section class="program program--light program--stress">
    <h2 class="program__title">STRESS RELIEF &amp; DEEP RELAXATION PROGRAM</h2>
    <p class="program__text">Our Program gently uncovers the true source of your<br>stress, and helps you reconnect to a natural inner calm.<br>We teach you self hypnosis so that you have the tools to<br>continue your experience.</p>
    <p class="program__sessions">Number of Sessions: 3+</p>
  </section>

  <p class="footer-note">All Programs include take home CD’s personally recorded by<br>our therapists, using advanced hypnotic techniques.</p>
</body>
</html>
```